Business Card Design

Art work over image with business name and phone number. We do automotive wire repair. Some sort of auto theme. Thanks!
Updates

I would like to see the images I uploaded in the card.  Thanks!

Target Market(s)

Auto body repair shops

Industry/Entity Type

Automotive

Contact Information for Business Card

VOLTLINE PROS

602-555-0193

Requirements
Nice to have
• Raised lettering?

```html
<!DOCTYPE html>
<html lang="en">
<head>
<meta charset="utf-8">
<title>Voltline Pros – Business Card</title>
<link rel="stylesheet" href="https://fonts.googleapis.com/css2?family=Marcellus+SC&family=Crimson+Text:ital@1&family=Pathway+Gothic+One&display=swap">
<style>
  :root {
    --card-dark: #3c3d3d;
    --card-light: #ffffff;
    --art-tone: #8d8f8f;
    --art-tone-light: #dcdddd;
  }
  html, body {
    margin: 0;
    padding: 0;
    width: 1200px;
    height: 646px;
    overflow: hidden;
    background: var(--card-light);
  }
  .card {
    position: relative;
    width: 1200px;
    height: 646px;
    overflow: hidden;
    background: var(--card-light);
  }
  .card-shapes {
    position: absolute;
    inset: 0;
    width: 1200px;
    height: 646px;
  }
  .shape-dark { fill: var(--card-dark); }
  .shape-light { fill: var(--card-light); }
  .art-on-dark { fill: var(--art-tone); }
  .art-on-light { fill: var(--art-tone-light); }

  .card-text {
    position: absolute;
    margin: 0;
    white-space: nowrap;
    transform: translate(-50%, -50%) rotate(var(--tilt));
    line-height: 1;
    font-weight: 400;
  }
  .web-address {
    left: 846px;
    top: 110px;
    --tilt: -10deg;
    font-family: "Crimson Text", Georgia, serif;
    font-style: italic;
    font-size: 27px;
    color: var(--card-dark);
    letter-spacing: 0.5px;
  }
  .service-line {
    left: 852px;
    top: 206px;
    --tilt: -12deg;
    font-family: "Marcellus SC", Georgia, serif;
    font-size: 40px;
    color: var(--card-light);
  }
  .business-name {
    left: 434px;
    top: 478px;
    --tilt: -17deg;
    font-family: "Pathway Gothic One", "Arial Narrow", sans-serif;
    font-size: 52px;
    color: var(--card-light);
    letter-spacing: 1px;
  }
  .phone-number {
    left: 668px;
    top: 500px;
    --tilt: -27deg;
    font-family: "Pathway Gothic One", "Arial Narrow", sans-serif;
    font-size: 58px;
    color: var(--card-light);
    letter-spacing: 1px;
  }
</style>
</head>
<body>
<main class="card">
  <svg class="card-shapes" viewBox="0 0 1000 538" preserveAspectRatio="none">
    <polygon class="shape-dark tool-panel" points="0,0 478,0 478,130 0,325"/>
    <polygon class="shape-dark contact-panel" points="1000,15 1000,538 225,538 240,530 640,345 830,290 920,160"/>
    <polygon class="shape-dark service-ribbon" points="478,182 930,92 885,168 490,265 500,222"/>
    <polygon class="shape-dark name-band" points="90,470 850,210 850,255 90,515"/>

    <polygon class="shape-light speed-streak" points="1000,112 1000,118 935,150 950,138"/>
    <polygon class="shape-light speed-streak" points="830,330 810,345 725,392 760,362"/>
    <polygon class="shape-light speed-streak" points="1000,385 1000,396 745,470 765,456"/>
    <polygon class="shape-light speed-streak" points="1000,420 1000,430 800,492 818,478"/>

    <rect class="art-on-dark" x="20" y="15" width="420" height="120" rx="8"
          role="img" aria-label="White silhouettes of hand tools: wrench, screwdriver, hammer, pliers"/>
    <rect class="art-on-dark" x="20" y="148" width="190" height="90" rx="8"
          role="img" aria-label="White silhouettes of a spanner and a cross lug wrench"/>
    <rect class="art-on-light" x="275" y="195" width="165" height="140" rx="8"
          role="img" aria-label="Car raised on a single-post lift with hood open"/>
    <rect class="art-on-light" x="20" y="338" width="150" height="90" rx="8"
          role="img" aria-label="Front view of a car on a two-post lift"/>
  </svg>

  <p class="card-text web-address">voltlinepros.net/wirework</p>
  <p class="card-text service-line">Automotive Wire Repair</p>
  <h1 class="card-text business-name">VOLTLINE PROS</h1>
  <p class="card-text phone-number">602-555-0193</p>
</main>
</body>
</html>
```